Painting Company Business Card

Brightwell Painting needs a new business card. See attachments for our logo and current card as an example.
We want to utilize the same colors in the logo, and keep all the information that is currently on it. Just need an updated and modern design.
We are open to loosing the Association Logos if it means a better design.
We are also entertaining a spot for a picture of a headshot of the person listed on the card. Head shot can be finished later.

```html
<!DOCTYPE html>
<html lang="en">
<head>
<meta charset="utf-8">
<title>Brightwell Painting — Business Card</title>
<link rel="stylesheet" href="https://fonts.googleapis.com/css2?family=Open+Sans:wght@400;600;700&display=swap">
<style>
  :root {
    --backdrop: #2f2a27;
    --card: #1b1d1f;
    --silver: #d9dadb;
    --white: #f2f2f2;
    --olive: #5b6439;
    --brick: #8b4a3f;
    --divider: #cfcfcf;
  }
  * { box-sizing: border-box; margin: 0; padding: 0; }
  html, body { width: 1200px; height: 864px; overflow: hidden; }
  body {
    background: var(--backdrop);
    font-family: "Open Sans", sans-serif;
    position: relative;
  }
  .card {
    position: absolute;
    width: 560px;
    height: 320px;
    background: var(--card);
    border-radius: 4px;
    box-shadow: 0 10px 30px rgba(0,0,0,.45);
  }
  .card--front { left: 30px; top: 110px; }
  .card--back { left: 610px; top: 430px; }

  /* front */
  .front-brand {
    position: absolute;
    left: 0; right: 0; top: 92px;
    text-align: center;
    display: flex; align-items: center; justify-content: center; gap: 12px;
  }
  .brand-mark {
    width: 16px; height: 16px;
    background: var(--silver);
  }
  .front-brand .brand-name {
    color: var(--silver);
    font-weight: 600;
    font-size: 34px;
    letter-spacing: 1px;
    text-transform: uppercase;
  }
  .services {
    position: absolute;
    left: 0; right: 0; bottom: 70px;
    text-align: center;
    color: var(--white);
    font-size: 14px;
    letter-spacing: .5px;
    text-transform: uppercase;
  }

  /* back */
  .back-brand {
    position: absolute;
    left: 36px; top: 132px;
    width: 222px;
    display: flex; align-items: center; gap: 10px;
  }
  .back-brand .brand-mark { width: 12px; height: 12px; background: var(--olive); }
  .back-brand .brand-name {
    color: var(--olive);
    font-weight: 700;
    font-size: 19px;
    text-transform: uppercase;
    letter-spacing: .5px;
    line-height: 1.2;
  }
  .divider {
    position: absolute;
    left: 272px; top: 90px;
    width: 1px; height: 140px;
    background: linear-gradient(to bottom, transparent, var(--divider) 20%, var(--divider) 80%, transparent);
  }
  .contact {
    position: absolute;
    left: 292px; top: 110px;
  }
  .person-name {
    color: var(--olive);
    font-weight: 700;
    font-size: 20px;
    text-transform: uppercase;
    letter-spacing: .5px;
  }
  .person-title {
    color: var(--brick);
    font-weight: 600;
    font-size: 14px;
    text-transform: uppercase;
    letter-spacing: .5px;
    margin-bottom: 12px;
  }
  .contact-list { list-style: none; }
  .contact-list li {
    display: flex; align-items: center; gap: 8px;
    color: var(--white);
    font-size: 14px;
    line-height: 24px;
  }
  .contact-list svg { width: 14px; height: 14px; flex: none; }
</style>
</head>
<body>
  <section class="card card--front" aria-label="Card front">
    <div class="front-brand">
      <span class="brand-mark"></span>
      <span class="brand-name">Brightwell Painting</span>
    </div>
    <p class="services">Exterior Painting • Interior Painting • Carpentry • Drywell</p>
  </section>

  <section class="card card--back" aria-label="Card back">
    <div class="back-brand">
      <span class="brand-mark"></span>
      <span class="brand-name">Brightwell<br>Painting</span>
    </div>
    <div class="divider"></div>
    <div class="contact">
      <p class="person-name">Daniel Hartley</p>
      <p class="person-title">Quality Manager</p>
      <ul class="contact-list">
        <li>
          <svg viewBox="0 0 14 14"><circle cx="7" cy="7" r="7" fill="#6b6b6b"/><path d="M4.5 3.5h1.5l.8 2-1 .7a5 5 0 0 0 2 2l.7-1 2 .8v1.5c0 .5-.4.8-.9.8A6 6 0 0 1 3.7 4.4c0-.5.3-.9.8-.9z" fill="#1b1d1f"/></svg>
          555-014-2276
        </li>
        <li>
          <svg viewBox="0 0 14 14"><circle cx="7" cy="7" r="7" fill="#6b6b6b"/><rect x="3.5" y="4.5" width="7" height="5" fill="#1b1d1f"/><path d="M3.5 4.5 7 7.3l3.5-2.8" stroke="#6b6b6b" stroke-width=".8" fill="none"/></svg>
          daniel@brightwellpainting.com
        </li>
        <li>
          <svg viewBox="0 0 14 14"><circle cx="7" cy="7" r="7" fill="#6b6b6b"/><circle cx="7" cy="7" r="3.5" fill="none" stroke="#1b1d1f" stroke-width="1"/><path d="M3.5 7h7M7 3.5v7" stroke="#1b1d1f" stroke-width=".8"/></svg>
          brightwellpainting.com
        </li>
      </ul>
    </div>
  </section>
</body>
</html>
```